Business Card Design Project

i need a bussines car design
Veltra Clinical Hypnotherapy

Gordon Wexley
Psychotherapy & Hypnosis

64029381 /0427956120

back of the card appoinment space.

file was provided on a PDF, LOgo , use the blu colorsa as well , elegant, clear,

Target Market(s)

young professional, caucasian , young mothers.

Industry/Entity Type

Business

```html
<!DOCTYPE html>
<html lang="en">
<head>
<meta charset="utf-8">
<title>Veltra Clinical Hypnotherapy – Business Card</title>
<link href="https://fonts.googleapis.com/css2?family=Questrial&family=Arimo:wght@400;700&display=swap" rel="stylesheet">
<style>
  :root {
    --stage: #e9ebee;
    --card: #ffffff;
    --card-shade: #eef1f5;
    --blue: #1f74c4;
    --blue-deep: #155a9e;
    --blue-light: #3f8fd8;
    --ink: #3b3f45;
    --ink-soft: #6a6f76;
    --photo-top: #c9c2b6;
    --photo-bottom: #e8dccb;
    --badge: #7fae3a;
  }
  * { box-sizing: border-box; margin: 0; padding: 0; }
  html, body { width: 1200px; height: 880px; overflow: hidden; }
  body {
    background: var(--stage);
    font-family: "Questrial", "Century Gothic", sans-serif;
    color: var(--ink);
    position: relative;
  }

  .card {
    position: absolute;
    background: linear-gradient(160deg, var(--card) 40%, var(--card-shade));
    box-shadow: 0 6px 18px rgba(0,0,0,.18);
    overflow: hidden;
  }

  /* ---------- Front ---------- */
  .card--front { left: 96px; top: 140px; width: 600px; height: 367px; }

  .portrait {
    position: absolute; left: 20px; top: 30px; width: 250px; height: 337px;
    background: linear-gradient(180deg, var(--photo-top), var(--photo-bottom));
    border-radius: 120px 120px 0 0;
  }
  .member-badge {
    position: absolute; left: 26px; top: 270px; width: 48px; height: 48px;
    border-radius: 50%; background: var(--badge);
  }

  .brand { position: absolute; left: 272px; top: 34px; display: flex; align-items: center; gap: 10px; }
  .brand__dot { width: 26px; height: 26px; border-radius: 50%; background: var(--blue); }
  .brand__name { font-size: 25px; color: var(--ink); letter-spacing: .2px; }
  .brand__url {
    position: absolute; left: 308px; top: 70px; font-size: 11px;
    color: var(--ink-soft); letter-spacing: 1px; font-weight: 700;
  }

  .bar {
    position: absolute; height: 34px; color: #fff; display: flex; align-items: center;
    padding-left: 30px; border-radius: 0 17px 17px 0;
  }
  .bar--name {
    left: 262px; top: 112px; width: 290px; background: var(--blue);
    font-size: 24px; letter-spacing: .3px;
  }
  .bar--role {
    left: 250px; top: 150px; width: 330px; background: var(--blue-light);
    font-size: 20px; padding-left: 28px;
  }
  .bar--phone {
    left: 250px; width: 320px; height: 40px; border-radius: 0 20px 20px 0;
    background: var(--blue-deep); font-size: 25px; letter-spacing: 1px; padding-left: 80px;
  }
  .bar--landline { top: 240px; }
  .bar--mobile { top: 294px; }
  .bar__icon {
    position: absolute; right: 2px; top: 2px; width: 36px; height: 36px; border-radius: 50%;
    background: #fff; display: flex; align-items: center; justify-content: center;
  }

  /* ---------- Back ---------- */
  .card--back {
    left: 736px; top: 40px; width: 367px; height: 600px;
    font-family: "Arimo", Arial, sans-serif;
  }
  .back__brand { position: absolute; left: 26px; top: 28px; display: flex; align-items: center; gap: 8px; }
  .back__brand .brand__dot { width: 22px; height: 22px; }
  .back__brand .brand__name { font-family: "Questrial", sans-serif; font-size: 21px; }
  .back__url { position: absolute; left: 56px; top: 56px; font-size: 9px; color: var(--ink-soft); letter-spacing: .6px; }

  .back__contact { position: absolute; left: 26px; top: 96px; font-size: 14px; line-height: 1.45; color: var(--ink); }

  .back__title {
    position: absolute; left: 26px; top: 160px; font-size: 27px; font-weight: 700; color: var(--blue);
  }

  .appointments { position: absolute; left: 26px; top: 214px; list-style: none; width: 318px; }
  .appointments li {
    display: flex; align-items: flex-end; height: 44px; font-size: 15px; color: var(--ink); gap: 4px;
  }
  .appointments .blank { border-bottom: 1px solid var(--ink); display: inline-block; height: 16px; }
  .blank--time { width: 34px; }
  .blank--date { flex: 1; }
  .blank--d { width: 22px; }

  .back__band {
    position: absolute; left: 0; bottom: 0; width: 100%; height: 66px; background: var(--blue);
    color: #fff; padding: 10px 18px; font-size: 9.5px; line-height: 1.35;
  }
  .back__band strong { display: block; margin-top: 4px; font-size: 12px; }
</style>
</head>
<body>

<section class="card card--front" aria-label="Business card front">
  <div class="portrait" role="img" aria-label="Portrait photograph of Gordon Wexley"></div>
  <div class="member-badge" role="img" aria-label="Professional association badge"></div>

  <div class="brand">
    <span class="brand__dot"></span>
    <span class="brand__name">Veltra Hypnotherapy</span>
  </div>
  <div class="brand__url">www.veltraclinicalhypnotherapy.com.au</div>

  <div class="bar bar--name">Gordon Wexley</div>
  <div class="bar bar--role">Psychotherapy &amp; Hypnosis</div>

  <div class="bar bar--phone bar--landline">64 029 381
    <span class="bar__icon">
      <svg width="22" height="22" viewBox="0 0 24 24" aria-hidden="true">
        <path fill="#155a9e" d="M6.6 10.8a15 15 0 0 0 6.6 6.6l2.2-2.2a1 1 0 0 1 1-.25 11.4 11.4 0 0 0 3.6.57 1 1 0 0 1 1 1V20a1 1 0 0 1-1 1A17 17 0 0 1 3 4a1 1 0 0 1 1-1h3.5a1 1 0 0 1 1 1c0 1.25.2 2.45.57 3.57a1 1 0 0 1-.25 1z"/>
      </svg>
    </span>
  </div>
  <div class="bar bar--phone bar--mobile">0427 956 120
    <span class="bar__icon">
      <svg width="20" height="22" viewBox="0 0 20 24" aria-hidden="true">
        <rect x="4" y="1" width="12" height="22" rx="2" fill="none" stroke="#155a9e" stroke-width="2"/>
        <rect x="6.5" y="4" width="7" height="7" fill="#155a9e"/>
        <circle cx="10" cy="19" r="1.4" fill="#155a9e"/>
      </svg>
    </span>
  </div>
</section>

<section class="card card--back" aria-label="Business card back">
  <div class="back__brand">
    <span class="brand__dot"></span>
    <span class="brand__name">Veltra Hypnotherapy</span>
  </div>
  <div class="back__url">www.veltraclinicalhypnotherapy.com.au</div>

  <p class="back__contact">By Appointment · Phone: 0427 956 120<br>118 Merrow rd Kelmarsh,</p>

  <h2 class="back__title">Your Appointments</h2>

  <ol class="appointments">
    <li>1. <span class="blank blank--time"></span>am/pm <span class="blank blank--date"></span> <span class="blank blank--d"></span>/<span class="blank blank--d"></span>/<span class="blank blank--d"></span></li>
    <li>2. <span class="blank blank--time"></span>am/pm <span class="blank blank--date"></span> <span class="blank blank--d"></span>/<span class="blank blank--d"></span>/<span class="blank blank--d"></span></li>
    <li>3. <span class="blank blank--time"></span>am/pm <span class="blank blank--date"></span> <span class="blank blank--d"></span>/<span class="blank blank--d"></span>/<span class="blank blank--d"></span></li>
    <li>4. <span class="blank blank--time"></span>am/pm <span class="blank blank--date"></span> <span class="blank blank--d"></span>/<span class="blank blank--d"></span>/<span class="blank blank--d"></span></li>
    <li>5. <span class="blank blank--time"></span>am/pm <span class="blank blank--date"></span> <span class="blank blank--d"></span>/<span class="blank blank--d"></span>/<span class="blank blank--d"></span></li>
    <li>6. <span class="blank blank--time"></span>am/pm <span class="blank blank--date"></span> <span class="blank blank--d"></span>/<span class="blank blank--d"></span>/<span class="blank blank--d"></span></li>
  </ol>

  <div class="back__band">
    To reschedule your appointment, please SMS or phone 0427 956 120 at least 24 hours prior to your allocated time. Thank you.
    <strong>CTPB Registration No. CTP048215</strong>
  </div>
</section>

</body>
</html>
```